Company Pull Up Banner for Hosting a Japanese Student in Western Australia!

Wren Educational Tours is an educational tourism and homestay management company based in Western Australia. We specialise in cultural immersion programs that connect Japanese students with Australian students and host families, through real-life, immersive experiences.
Tag line: Sharing Cultures. Creating Friendships.
Website: wrenel.com.au
Objective:
Create a vibrant and engaging company banner to promote homestay hosting opportunities in Western Australia. The target audience is families with children. The design should exude warmth, friendliness, and a sense of community. Our aim is to increase brand awareness and the opportunity to host a Japanese student. Please incorporate company logo as well as Japanese pop culture references in a fun and natural way. (Nothing related to Vornakk please). Typically, we use photos in our marketing material to add warmth and engagement however we would consider the option to convey our message graphically.
Key Information:
- Target Audience: Families with children in Western Australia
- Location: Western Australia
- Client's Logo: See file attached
Design Elements:
1. Warmth and Friendliness:
- Use warm and inviting colours such as oranges, yellows, etc
- Use friendly and approachable fonts for any text elements.
2. Inclusion of Client's Logo:
- Ensure prominent placement of company logo
- Maintain logo colours and fonts for brand consistency
3. Graphics and Imagery:
- Option to include joyful graphics of families, children, and Japanese pop culture references.
- Photos of smiling families can be incorporated. Please see image reference attached.
Dimensions and Format:
- Dimensions: 845mm W x 2000mm L (Include a 5mm bleed margin on width. 10mm to top and 100mm to bottom).
- Format: High-resolution file suitable for printing (PDF, JPEG, or other standard formats)
Additional Notes:
- Ensure that the design aligns with the family-friendly and community-oriented theme.
- The overall tone should be positive, welcoming, and inclusive.
By incorporating these elements, the goal is to create a visually appealing banner that effectively communicates the warmth of the event to the target audience while maintaining brand identity.
Target Market(s)
Families with children in Western Australia
Industry/Entity Type
Tourism and Education
Requirements
Must have
- Design Elements: 1. Warmth and Friendliness: - Use warm and inviting colours such as oranges, yellows, etc - Use friendly and approachable fonts for any text elements. 2. Inclusion of Client's Logo: - Ensure prominent placement of company logo - Maintain logo colours and fonts for brand consistency 3. Graphics and Imagery: - include graphics of Japanese pop culture references. - Photos of smiling families can be incorporated. Please see image reference attached.

```html
<!DOCTYPE html>
<html lang="en">
<head>
<meta charset="utf-8">
<title>Wren Educational Tours – Pull Up Banner</title>
<link href="https://fonts.googleapis.com/css2?family=Poppins:wght@400;500;600;700;800&display=swap" rel="stylesheet">
<style>
  :root {
    --red: #e01b1b;
    --deep-red: #b5100f;
    --yellow: #fcd116;
    --gold: #f2b705;
    --ink: #1a1a1a;
    --navy: #1f2d5c;
    --white: #ffffff;
    --stage: #f4f4f4;
  }
  * { margin: 0; padding: 0; box-sizing: border-box; }
  html, body { width: 1200px; height: 2550px; overflow: hidden; background: var(--stage); }
  body { font-family: "Poppins", sans-serif; position: relative; }

  .banner {
    position: absolute; left: 100px; top: 75px;
    width: 1000px; height: 2400px;
    background: var(--white);
    overflow: hidden;
    box-shadow: 0 10px 30px rgba(0,0,0,.18);
  }
  .banner-shapes { position: absolute; inset: 0; }

  .brand {
    position: absolute; left: 60px; top: 70px;
    display: flex; align-items: center; gap: 34px;
    color: var(--red);
  }
  .brand-mark { width: 150px; height: 150px; background: var(--red); }
  .brand-name { font-weight: 500; line-height: 1.05; }
  .brand-name .primary { display: block; font-size: 96px; }
  .brand-name .secondary { display: block; font-size: 38px; letter-spacing: 1px; }

  .tagline { position: absolute; left: 52px; top: 1262px; }
  .tagline-lead { font-size: 46px; font-weight: 700; color: var(--ink); line-height: 1; }
  .tagline-main { font-size: 112px; font-weight: 800; color: var(--red); line-height: 1; margin-top: 10px; letter-spacing: 1px; }
  .tagline-band {
    position: absolute; left: 52px; top: 1412px;
    width: 840px; height: 106px;
    background: var(--yellow);
    clip-path: polygon(0 0, 82% 0, 100% 100%, 0 100%);
  }
  .tagline-band span {
    display: block; padding-left: 16px;
    font-size: 100px; font-weight: 800; color: var(--ink); line-height: 106px;
  }

  .schools-label {
    position: absolute; left: 332px; top: 1548px;
    width: 336px; height: 62px;
    background: var(--red); color: var(--white);
    font-size: 36px; font-weight: 700; letter-spacing: 4px;
    text-align: center; line-height: 62px;
  }

  .schools {
    position: absolute; left: 40px; top: 1650px; width: 920px;
    display: grid; grid-template-columns: repeat(4, 1fr);
    row-gap: 60px;
  }
  .school { display: flex; flex-direction: column; align-items: center; gap: 14px; height: 180px; justify-content: center; }
  .school-shape { width: 110px; height: 110px; border-radius: 50%; background: var(--navy); }
  .school-shape.square { border-radius: 12px; }
  .school-name { font-size: 26px; font-weight: 600; color: var(--navy); text-align: center; line-height: 1.1; }

  .location {
    position: absolute; left: 0; top: 2118px; width: 100%;
    display: flex; justify-content: center; align-items: center; gap: 14px;
    font-size: 48px; font-weight: 700; color: var(--ink);
  }
  .location svg { width: 40px; height: 52px; }
  .website {
    position: absolute; left: 0; top: 2180px; width: 100%;
    text-align: center; font-size: 66px; font-weight: 700;
    letter-spacing: 5px; color: var(--ink);
  }
</style>
</head>
<body>
  <main class="banner">
    <svg class="banner-shapes" viewBox="0 0 1000 2400" width="1000" height="2400" aria-hidden="true">
      <defs>
        <linearGradient id="photoTone" x1="0" y1="0" x2="1" y2="1">
          <stop offset="0" stop-color="#6b2a22"/>
          <stop offset="0.45" stop-color="#c55a3e"/>
          <stop offset="1" stop-color="#8a1a14"/>
        </linearGradient>
        <linearGradient id="shardRed" x1="0" y1="0" x2="1" y2="1">
          <stop offset="0" stop-color="#ff3a2a"/>
          <stop offset="1" stop-color="#b5100f"/>
        </linearGradient>
      </defs>
      <polygon points="0,412 237,505 0,640" fill="var(--yellow)"/>
      <polygon points="0,600 1000,258 1000,930 0,1186" fill="url(#photoTone)" role="img" aria-label="Photo of smiling students and host family members posing together"/>
      <polygon points="470,1100 1000,900 1000,980 700,1110" fill="var(--yellow)"/>
      <polygon points="680,1124 784,1041 1000,928 1000,1392 784,1386" fill="url(#shardRed)"/>
      <polygon points="0,2255 433,2400 0,2400" fill="var(--yellow)"/>
      <polygon points="433,2400 1000,2202 1000,2400" fill="var(--deep-red)"/>
    </svg>

    <header class="brand">
      <div class="brand-mark"></div>
      <div class="brand-name">
        <span class="primary">Wren</span>
        <span class="secondary">EDUCATIONAL TOURS</span>
      </div>
    </header>

    <section class="tagline">
      <p class="tagline-lead">SHARING CULTURES</p>
      <p class="tagline-main">CREATING</p>
    </section>
    <div class="tagline-band"><span>FRIENDSHIPS</span></div>

    <h2 class="schools-label">OUR SCHOOLS</h2>

    <section class="schools">
      <div class="school"><div class="school-shape"></div><p class="school-name">Harrow Vale</p></div>
      <div class="school"><div class="school-shape"></div><p class="school-name">Ridgefern College</p></div>
      <div class="school"><div class="school-shape square"></div><p class="school-name">Eastfield High</p></div>
      <div class="school"><div class="school-shape"></div><p class="school-name">Ellenmoor College</p></div>
      <div class="school"><div class="school-shape square"></div><p class="school-name">Baxter College</p></div>
      <div class="school"><div class="school-shape"></div><p class="school-name">Kestrel High</p></div>
      <div class="school"><div class="school-shape square"></div><p class="school-name">Fairhaven College</p></div>
      <div class="school"><div class="school-shape"></div><p class="school-name">Juniper Fields</p></div>
    </section>

    <p class="location">
      <svg viewBox="0 0 40 52" aria-hidden="true">
        <path d="M20 2C10 2 3 9.5 3 19c0 12 17 30 17 30s17-18 17-30C37 9.5 30 2 20 2z" fill="none" stroke="var(--red)" stroke-width="5"/>
        <circle cx="20" cy="19" r="6" fill="var(--red)"/>
      </svg>
      WESTERN AUSTRALIA
    </p>
    <p class="website">www.wrenel.com.au</p>
  </main>
</body>
</html>
```